"Tales of Quiet Harbors" Book Cover Design

I am seeking a dynamic, modern, and professional cover design for a book focused on groundbreaking science that explores how a supplement called plasmalogens can revitalize the brain, prevent Alzheimer’s, and safeguard memories. The design should strike a balance between being visually appealing and conveying the seriousness of the topic.

Target Market(s)

The target audience includes individuals who are curious about cutting-edge science and proactive approaches to brain health, as well as those seeking to better understand how to protect their cognitive functions and memories. The cover should resonate with readers interested in health, science, and self-improvement, while reflecting the book’s informative and empowering tone.

Requirements
Must have
• The quotation across the top of the page (this is a placeholder for now, it will be changed eventually) and the author's name.
Should not have
• You don't need to use the puzzle idea!

```html
<!DOCTYPE html>
<html lang="en">
<head>
<meta charset="utf-8">
<title>Tales of Quiet Harbors — Book Cover</title>
<link rel="stylesheet" href="https://fonts.googleapis.com/css2?family=Montserrat:wght@400;700;800&display=swap">
<style>
  :root {
    --page-bg: #ffffff;
    --deep-blue: #2a4f8f;
    --steel-blue: #3d5f96;
    --navy: #1f3a6b;
    --amber: #f5a000;
    --warm-glow: #e0a030;
    --cream: #e9d6a8;
    --title-white: #ffffff;
    --ghost: rgba(255, 255, 255, 0.28);
  }
  * { margin: 0; padding: 0; box-sizing: border-box; }
  html, body {
    width: 1200px;
    height: 846px;
    overflow: hidden;
    background: var(--page-bg);
    font-family: "Montserrat", Arial, sans-serif;
  }
  .book-cover {
    position: absolute;
    left: 324px;
    top: 33px;
    width: 552px;
    height: 780px;
    overflow: hidden;
  }
  .cover-photo {
    position: absolute;
    inset: 0;
    background:
      radial-gradient(ellipse 55% 30% at 62% 0%, rgba(240, 170, 40, 0.85), transparent 70%),
      radial-gradient(ellipse 45% 35% at 0% 78%, rgba(230, 160, 40, 0.75), transparent 70%),
      radial-gradient(ellipse 40% 30% at 40% 92%, rgba(233, 214, 168, 0.8), transparent 70%),
      radial-gradient(ellipse 30% 50% at 92% 35%, rgba(225, 225, 230, 0.55), transparent 70%),
      linear-gradient(180deg, var(--steel-blue) 0%, var(--deep-blue) 45%, var(--navy) 75%, #4a5568 100%);
  }
  .author-name {
    position: absolute;
    top: 18px;
    left: 168px;
    font-size: 15px;
    font-weight: 400;
    letter-spacing: 0.5px;
    color: var(--title-white);
  }
  .tagline-marker {
    position: absolute;
    left: 0;
    top: 99px;
    width: 42px;
    height: 51px;
    background: var(--amber);
  }
  .tagline {
    position: absolute;
    left: 50px;
    top: 99px;
    font-size: 10.4px;
    line-height: 14px;
    font-weight: 400;
    text-transform: uppercase;
    color: var(--amber);
  }
  .title {
    position: absolute;
    left: 18px;
    top: 190px;
    font-weight: 700;
    font-size: 78px;
    line-height: 82px;
    text-transform: uppercase;
    color: var(--title-white);
    letter-spacing: -1px;
  }
  .title span { display: block; }
  .title .line-1 { padding-left: 6px; }
  .title .line-2 { padding-left: 110px; }
  .title .line-4 { padding-left: 0; }
  .title-echo {
    position: absolute;
    font-weight: 700;
    font-size: 78px;
    line-height: 82px;
    text-transform: uppercase;
    color: var(--ghost);
    letter-spacing: -1px;
  }
  .title-echo.echo-top { left: 215px; top: 190px; }
  .title-echo.echo-left { left: 8px; top: 272px; }
</style>
</head>
<body>
  <main class="book-cover">
    <div class="cover-photo" role="img" aria-label="Photograph of an elderly bearded man in glasses playing chess, blended with blue brain scan imagery and warm amber light"></div>

    <p class="author-name">AUTHOR</p>

    <div class="tagline-marker"></div>
    <p class="tagline">
      Groundbreaking science that explores<br>
      how a supplement called plasmalogens<br>
      can revitalize the brain,<br>
      prevent Alzheimer’s, and safeguard memories
    </p>

    <span class="title-echo echo-top" aria-hidden="true">OF</span>
    <span class="title-echo echo-left" aria-hidden="true">LES</span>

    <h1 class="title">
      <span class="line-1">Tales</span>
      <span class="line-2">Of</span>
      <span class="line-3">Quiet</span>
      <span class="line-4">Harbors</span>
    </h1>
  </main>
</body>
</html>
```